Cover-Design für Buch zum Thema Selbstmotivation
Zielgruppe
Ich bin Blogger und Autor und habe mich mit meinen Websites und Taschenbuch-Projekten ganz dem Thema Selbstmotivation verschrieben.
Mit meinem ersten Buch: 'Der Funke des inneren Antriebs!', möchte ich Lesern zu einer wirkungsvollen Fähigkeit Selbstmotivation verhelfen.
Das Taschenbuch mit Tipps und Methoden beschreibt, die Fähigkeit zur Selbstmotivation zu entwickeln.
Einmal angefangen entwickelt sich daraus eine besondere Eigendynamik, die Funke des inneren Antriebs und ist auch der Titel des Buches.
Ein einfaches und in seiner Art einzigartiges Konzept, bei dem die Lebensfreude mit entwickelt wird und ein wichtiges Element ist.
Begleitet mit diversen Übungen.
Ein Arbeitsheft zum Ausdrucken (PDF), kann bei Bedarf zusätzlich heruntergeladen werden.
Zielgruppe sind Frauen und Männer mittleren Alters, die mehr in sich spüren und eine Veränderung wünschen, jedoch irgendwie nicht vorankommen.
Aufgabenstellung
Das Design sollte an sich schon ansprechend und motivierend sein. Hell freundlich, ggf. mit Farbverläufen (Muster-Datei)
Bitte das Muster NICHT verwenden, da dieses ein Bild von Fotolunda ist und von anderen auch frei verwendet werden kann. Das Muster ist kein Muss. Es hat mich nur spontan angesprochen und habe es als 'Vorschaubild' auf meiner Website Lebkraft17.example verwendet.
Ggf. mit Foto des Autors
Titel: 'Der Funke des inneren Antriebs!'
Untertitel: Selbstmotivation könne wir lernen und ist eine der wertvollsten Investition in uns selbst.

```html
<!DOCTYPE html>
<html lang="de">
<head>
<meta charset="utf-8">
<title>Der Funke des inneren Antriebs! – Cover</title>
<link href="https://fonts.googleapis.com/css2?family=Advent+Pro:wght@300;500;600&family=Roboto:wght@400&display=swap" rel="stylesheet">
<style>
  :root {
    --teal: #029a91;
    --ink: #0a9690;
    --paper-top: #f1d690;
    --paper-bottom: #ebbd62;
    --stroke: #f2c560;
    --ball-dark: #0f5f5c;
    --ball-light: #8cbf86;
  }
  * { margin: 0; padding: 0; box-sizing: border-box; }
  html, body { width: 1200px; height: 684px; overflow: hidden; }
  body { background: var(--teal); position: relative; font-family: "Advent Pro", sans-serif; color: var(--ink); }

  .cover, .wrap {
    position: absolute;
    background: linear-gradient(180deg, var(--paper-top) 0%, #eecb7a 60%, var(--paper-bottom) 100%);
    box-shadow: 0 2px 4px rgba(0,0,0,.25);
  }
  .cover { left: 47px; top: 43px; width: 418px; height: 592px; }
  .wrap { left: 527px; top: 227px; width: 614px; height: 408px; }

  .artwork {
    position: absolute; left: 0; top: 0; width: 100%;
    background:
      radial-gradient(ellipse 80% 28% at 55% 78%, rgba(242,197,96,.9), rgba(242,197,96,0) 70%),
      linear-gradient(90deg, rgba(15,95,92,.0), rgba(15,95,92,0));
  }
  .artwork svg { display: block; width: 100%; height: 100%; }

  .title { position: absolute; font-weight: 600; line-height: 1.38; white-space: nowrap; letter-spacing: .5px; }
  .subtitle { position: absolute; font-weight: 300; white-space: nowrap; }
  .author { position: absolute; font-weight: 500; white-space: nowrap; }

  /* front cover */
  .cover .artwork { height: 200px; }
  .cover .title { left: 20px; top: 222px; font-size: 55px; line-height: 68px; }
  .cover .subtitle { left: 21px; top: 389px; font-size: 19px; line-height: 22px; }
  .cover .author { left: 0; width: 100%; text-align: center; top: 545px; font-size: 14px; }

  /* wraparound: back, spine, front */
  .wrap .back { position: absolute; left: 0; top: 0; width: 288px; height: 100%; }
  .wrap .spine { position: absolute; left: 288px; top: 0; width: 38px; height: 100%; border-left: 1px solid rgba(10,150,144,.12); border-right: 1px solid rgba(10,150,144,.12); }
  .wrap .front { position: absolute; left: 326px; top: 0; width: 288px; height: 100%; }

  .blurb { position: absolute; left: 39px; top: 24px; width: 212px; font-family: "Roboto", sans-serif; font-size: 6.6px; line-height: 10.3px; }
  .blurb p + p { margin-top: 10.3px; }

  .author-photo { position: absolute; left: 39px; top: 296px; width: 69px; height: 82px; background: linear-gradient(160deg, #f3efe9, #d9c3b4 55%, #6f6f78); }
  .author-name { position: absolute; left: 129px; top: 297px; font-size: 9.5px; font-weight: 500; }
  .author-bio { position: absolute; left: 129px; top: 314px; width: 124px; font-family: "Roboto", sans-serif; font-size: 6.4px; line-height: 11.6px; }

  .spine .artwork { height: 80px; }
  .spine-title { position: absolute; left: 4px; bottom: 20px; writing-mode: vertical-rl; transform: rotate(180deg); font-weight: 600; font-size: 13.5px; line-height: 15px; white-space: nowrap; }
  .spine-tagline { position: absolute; left: 21px; top: 126px; writing-mode: vertical-rl; transform: rotate(180deg); font-weight: 300; font-size: 7px; line-height: 7.6px; white-space: nowrap; height: 140px; }

  .front .artwork { height: 134px; }
  .front .title { left: 13px; top: 156px; font-size: 38px; line-height: 48px; }
  .front .subtitle { left: 14px; top: 268px; font-size: 13px; line-height: 15px; }
  .front .author { left: 0; width: 100%; text-align: center; top: 376px; font-size: 10px; }
</style>
</head>
<body>

<section class="cover" aria-label="Buchcover Vorderseite">
  <div class="artwork" role="img" aria-label="Aquarell-Illustration: fünf hängende türkisgrüne Kugeln eines Kugelstoßpendels vor einem gelben Pinselstrich">
    <svg viewBox="0 0 418 200" preserveAspectRatio="none" aria-hidden="true">
      <defs>
        <linearGradient id="ballTone" x1="0" x2="1">
          <stop offset="0" stop-color="var(--ball-dark)"/>
          <stop offset="1" stop-color="var(--ball-light)"/>
        </linearGradient>
      </defs>
      <rect x="55" y="100" width="320" height="58" rx="29" fill="url(#ballTone)" opacity=".55"/>
    </svg>
  </div>
  <h1 class="title">Der Funke des<br>inneren Antriebs!</h1>
  <p class="subtitle">Selbstmotivation können wir lernen und<br>ist die wertvollste Investition in uns selbst.</p>
  <p class="author">Konrad Brosantel</p>
</section>

<section class="wrap" aria-label="Buchumschlag mit Rückseite, Buchrücken und Vorderseite">
  <div class="back">
    <div class="blurb">
      <p>Jeder kann sein Leben meistern und in den Griff bekommen um seine persönlichen Ziele erreichen. Ein entscheidendes Element ist immer wieder die Fähigkeit zur Selbstmotivation. Nie war diese so gefragt wie heute. Doch geht die in diesem Taschenbuch angesprochene Selbstmotivation weiter als allgemein gefordert.</p>
      <p>Selbstmotivation können wir leicht erlernen und zu unserem ganz persönlichen Vorankommen nutzen.</p>
      <p>In einem in dieser Form einzigartigen, vierstufigen Konzept zeigt der Autor einen mit Lebensfreude begleiteten Weg auf, um die eigene Selbstmotivation zu wecken und auszubauen. Dabei ist die Lebensfreude ein wichtiger Erfolgsfaktor.</p>
      <p>Einmal dieses wegweisende Konzept kennengelernt, entwickelt sich daraus eine ganz besondere Energie: „Der Funke des inneren Antriebs!“ Damit erhält der Leser seinen persönlichen Schlüssel zu seinem Lebensglück.</p>
      <p>Unterstützt und begleitet wird dieses Konzept von fünfzig ausgewählten Übungen. Zusammengefasst in einem Arbeitsheft können sie bei Bedarf zusätzlich zum Ausdrucken heruntergeladen werden.</p>
    </div>
    <div class="author-photo" role="img" aria-label="Porträtfoto des Autors"></div>
    <p class="author-name">Konrad Brosantel</p>
    <p class="author-bio">Mit den Webseiten www.lebkraft17.example und www.funkenquelle.example, sowie seinen Taschenbüchern und E-Books, hat sich Konrad Brosantel als Blogger und Autor, ganz dem Thema Selbstmotivation verschrieben.</p>
  </div>

  <div class="spine">
    <div class="artwork" role="img" aria-label="Illustration: eine hängende türkisgrüne Aquarellkugel">
      <svg viewBox="0 0 38 80" preserveAspectRatio="none" aria-hidden="true">
        <circle cx="19" cy="62" r="15" fill="var(--ball-dark)" opacity=".6"/>
      </svg>
    </div>
    <p class="spine-tagline">Selbstmotivation können wir lernen und<br>ist die wertvollste Investition in uns selbst.</p>
    <p class="spine-title">Der Funke des<br>inneren Antriebs!</p>
  </div>

  <div class="front">
    <div class="artwork" role="img" aria-label="Aquarell-Illustration: fünf hängende türkisgrüne Kugeln eines Kugelstoßpendels vor einem gelben Pinselstrich">
      <svg viewBox="0 0 288 134" preserveAspectRatio="none" aria-hidden="true">
        <rect x="38" y="68" width="220" height="40" rx="20" fill="url(#ballTone)" opacity=".55"/>
      </svg>
    </div>
    <h2 class="title">Der Funke des<br>inneren Antriebs!</h2>
    <p class="subtitle">Selbstmotivation können wir lernen und<br>ist die wertvollste Investition in uns selbst.</p>
    <p class="author">Konrad Brosantel</p>
  </div>
</section>

</body>
</html>
```